Lift Every Ledger Through Chairside Trust

Design a cover for this book which is designed to help a business go from it's current revenue and treatment acceptance to double (2X) that success and those metrics.

```html
<!DOCTYPE html>
<html lang="en">
<head>
<meta charset="utf-8">
<title>Lift Every Ledger Through Chairside Trust — Book Cover</title>
<link rel="stylesheet" href="https://fonts.googleapis.com/css2?family=Archivo+Black&display=swap">
<style>
  :root {
    --page-bg: #ffffff;
    --teal-top: #4fb2ae;
    --teal-bottom: #0ea19c;
    --photo-top: #4f79bf;
    --photo-mid: #1b3165;
    --photo-bottom: #8ba4d0;
    --ink-light: #ffffff;
  }
  html, body {
    margin: 0;
    padding: 0;
    width: 1200px;
    height: 1200px;
    overflow: hidden;
    background: var(--page-bg);
  }
  .book-cover {
    position: absolute;
    left: 337px;
    top: 187px;
    width: 523px;
    height: 785px;
    display: block;
  }
  .cover-title,
  .cover-author {
    font-family: "Archivo Black", "Arial Black", sans-serif;
    fill: var(--ink-light);
    text-anchor: middle;
  }
</style>
</head>
<body>
  <svg class="book-cover" viewBox="0 0 523 785" xmlns="http://www.w3.org/2000/svg">
    <defs>
      <linearGradient id="tealBand" x1="0" y1="0" x2="0" y2="1">
        <stop offset="0" stop-color="var(--teal-top)"/>
        <stop offset="1" stop-color="var(--teal-bottom)"/>
      </linearGradient>
      <linearGradient id="photoTone" x1="0" y1="0" x2="0" y2="1">
        <stop offset="0" stop-color="var(--photo-top)"/>
        <stop offset="0.45" stop-color="#3a5fa6"/>
        <stop offset="0.68" stop-color="var(--photo-mid)"/>
        <stop offset="0.8" stop-color="#5f79ab"/>
        <stop offset="1" stop-color="var(--photo-bottom)"/>
      </linearGradient>
    </defs>

    <rect class="cover-base" width="523" height="785" fill="url(#tealBand)"/>

    <path class="cover-photo" role="img"
          aria-label="Blue-toned photo of a business team meeting around a table with a printed revenue report in the foreground"
          d="M0 0 H387 C450 50 505 140 523 215 V525 C470 660 320 770 157 785 H0 Z"
          fill="url(#photoTone)"/>

    <ellipse class="title-ring" cx="263" cy="316" rx="237" ry="225"
             fill="none" stroke="var(--ink-light)" stroke-width="1.6"/>

    <text class="cover-title" x="263" y="250" font-size="92">LIFT</text>
    <text class="cover-title" x="263" y="304" font-size="50">EVERY</text>
    <text class="cover-title" x="263" y="344" font-size="36">LEDGER THROUGH</text>
    <text class="cover-title" x="263" y="382" font-size="33">CHAIRSIDE TRUST</text>

    <text class="cover-author" x="263" y="429" font-size="16">AUTHOR</text>
    <text class="cover-author" x="263" y="449" font-size="16">NAME AND SURNAME</text>
  </svg>
</body>
</html>
```